Painting Contractor Business Card Design

We are looking for a cool, bold, modern, polished, business card design. We are a high-end residential painting contractor. Please incorporate our logo and keep with our green/black color scheme. We are interested in seeing 2-sided and 1-sided options. Thank you very much!

Industry/Entity Type

Business

Contact Information for Business Card

Info for the card:
Dale Ormsby
mobile 206-555-0193
email dale@tallowbrookpainting.net
web www.tallowbrookpainting.net

```html
<!DOCTYPE html>
<html lang="en">
<head>
<meta charset="utf-8">
<title>Tallowbrook Painting – Business Cards</title>
<link href="https://fonts.googleapis.com/css2?family=Montserrat:wght@400;600;700&family=Open+Sans:wght@400;700&display=swap" rel="stylesheet">
<style>
  :root {
    --canvas: #e9e6e1;
    --green: #3fbf5a;
    --blue: #1f7fc8;
    --blue-name: #1d6fb8;
    --white: #ffffff;
    --black: #0c0f0e;
    --black-soft: #1b1f1e;
    --ink: #141414;
    --brand-green: #4cc25a;
  }
  * { margin: 0; padding: 0; box-sizing: border-box; }
  html, body {
    width: 1200px; height: 1023px; overflow: hidden;
    background: var(--canvas);
  }
  .canvas { position: relative; width: 1200px; height: 1023px; }

  .card {
    position: absolute;
    width: 600px; height: 343px;
    border-radius: 4px;
    overflow: hidden;
    box-shadow: 0 10px 28px rgba(0,0,0,0.22);
  }

  /* Front card */
  .card-front { left: 70px; top: 110px; background: var(--white); }
  .card-front .front-art { position: absolute; inset: 0; width: 100%; height: 100%; }
  .contact {
    position: absolute; left: 34px; bottom: 34px;
    font-family: "Open Sans", Arial, sans-serif;
    color: var(--white);
  }
  .contact-name {
    font-weight: 700; font-size: 21px;
    color: var(--blue-name);
    margin-bottom: 8px;
  }
  .contact-line {
    display: flex; align-items: center; gap: 7px;
    font-size: 13px; line-height: 20px;
  }
  .contact-line svg { width: 12px; height: 12px; flex: none; }
  .front-brand {
    position: absolute; right: 28px; bottom: 40px;
    display: flex; align-items: center; gap: 8px;
  }
  .brand-square { width: 18px; height: 18px; background: var(--brand-green); flex: none; }
  .brand-name {
    font-family: "Montserrat", Arial, sans-serif;
    font-weight: 700; font-size: 18px; letter-spacing: 0.3px;
    color: var(--ink);
    white-space: nowrap;
  }

  /* Back card */
  .card-back {
    left: 560px; top: 560px;
    background: linear-gradient(150deg, var(--black-soft) 0%, var(--black) 60%);
  }
  .back-brand {
    position: absolute; left: 0; right: 0; top: 50%;
    transform: translateY(-50%);
    text-align: center;
    font-family: "Montserrat", Arial, sans-serif;
    font-weight: 600; font-size: 30px; letter-spacing: 2px;
    color: var(--brand-green);
  }
</style>
</head>
<body>
<main class="canvas">

  <section class="card card-front" aria-label="Business card front">
    <svg class="front-art" viewBox="0 0 600 343" preserveAspectRatio="none">
      <defs>
        <linearGradient id="greenFill" x1="0" y1="0" x2="1" y2="1">
          <stop offset="0" stop-color="#5bcf6a"/>
          <stop offset="1" stop-color="#34b450"/>
        </linearGradient>
        <linearGradient id="patternTone" x1="0" y1="0" x2="1" y2="0">
          <stop offset="0" stop-color="#7fd98a" stop-opacity="0.3"/>
          <stop offset="1" stop-color="#b8e86a" stop-opacity="0.12"/>
        </linearGradient>
      </defs>
      <path d="M0 0 H600 V60 C480 56 435 115 385 190 C345 252 318 305 304 343 H0 Z" fill="var(--blue)"/>
      <path d="M0 0 H600 V42 C470 40 420 100 370 180 C330 245 303 300 288 343 H0 Z" fill="url(#greenFill)"/>
      <rect role="img" aria-label="Faint repeating brand-stripe pattern on the green field" x="0" y="0" width="330" height="170" fill="url(#patternTone)"/>
    </svg>

    <div class="contact">
      <p class="contact-name">Dale Ormsby</p>
      <p class="contact-line">
        <svg viewBox="0 0 16 16" aria-hidden="true"><path d="M3 1h3l1.5 4-2 1.2a9 9 0 0 0 4.3 4.3L11 8.5l4 1.5v3a2 2 0 0 1-2 2A12 12 0 0 1 1 3a2 2 0 0 1 2-2z" fill="#ffffff"/></svg>
        206-555-0193
      </p>
      <p class="contact-line">
        <svg viewBox="0 0 16 16" aria-hidden="true"><rect x="1" y="3" width="14" height="10" rx="1" fill="#ffffff"/><path d="M1.5 3.5 8 9l6.5-5.5" stroke="#3fbf5a" stroke-width="1.4" fill="none"/></svg>
        dale@tallowbrookpainting.net
      </p>
      <p class="contact-line">
        <svg viewBox="0 0 16 16" aria-hidden="true"><circle cx="8" cy="8" r="6.5" fill="none" stroke="#ffffff" stroke-width="1.4"/><ellipse cx="8" cy="8" rx="2.8" ry="6.5" fill="none" stroke="#ffffff" stroke-width="1.2"/><path d="M1.5 8h13" stroke="#ffffff" stroke-width="1.2"/></svg>
        www.tallowbrookpainting.net
      </p>
    </div>

    <div class="front-brand">
      <span class="brand-square" aria-hidden="true"></span>
      <span class="brand-name">TALLOWBROOK PAINTING</span>
    </div>
  </section>

  <section class="card card-back" aria-label="Business card back">
    <p class="back-brand">TALLOWBROOK PAINTING</p>
  </section>

</main>
</body>
</html>
```